Website redesign for PR company

We currently have a Squarespace site, which has been sufficient during the start up stage of our public relations business. I would be interested to know whether there are options within the Squarespace functionality to dramatically improve the look of our site, or whether you recommend a full redesign using another web service.

I would like the designer to offer some suggestions for improvements to the current site and/or provide designs for a new site.

I would like for us to have an ongoing relationship keeping our site up to date. Our current site is at www.quill-example.co.nz

Target Market(s)

New Zealand primarily, government and commercial clients

Industry/Entity Type

public relations

Coding

Coded - Design and coding required

Number of Pages Required

5+ page

Requirements
Must have
• Quill Blue: R38 G34 B98 / #262261 / C100 M100 Y25 K25 Quill Orange: R247 G148 B29 / #f7931d / C0 M50 Y100 K0 Pink: R249 G181 B178 / #f8b4b2 / C0 M25 Y25 K0No stock imagery, use of our profile photos as on current site and custom graphics only.
Should not have
• stock images

```html
<!DOCTYPE html>
<html lang="en">
<head>
<meta charset="utf-8">
<title>Quill Communications — People with expertise</title>
<link href="https://fonts.googleapis.com/css2?family=Poppins:wght@300;400;500;600;700&display=swap" rel="stylesheet">
<style>
:root{
  --quill-blue:#231f5c;
  --quill-orange:#f47424;
  --ink:#222;
  --muted:#666;
  --faint:#eef0f4;
  --white:#fff;
}
*{margin:0;padding:0;box-sizing:border-box}
html,body{width:1200px;height:4812px;overflow:hidden;background:var(--white)}
body{font-family:'Poppins',sans-serif;color:var(--ink)}
.page{position:relative;width:1200px;height:4812px;overflow:hidden}
.abs{position:absolute}
.slants{position:absolute;left:0;top:0;width:1200px;height:4812px;pointer-events:none}

/* header */
.brand{left:112px;top:30px;font-size:54px;font-weight:700;color:var(--quill-blue);letter-spacing:-1px;line-height:1}
.topbar{right:112px;top:36px;display:flex;align-items:center;gap:26px;font-size:13.5px;color:#333}
.topbar .ic{display:inline-flex;align-items:center;gap:7px}
.topbar .home{color:var(--quill-orange);font-weight:500}
.topbar .about{font-weight:500;color:var(--quill-blue)}
.btn-contact{background:var(--quill-orange);color:#fff;padding:11px 16px;border-radius:3px;font-weight:500;font-size:13px}
.mainnav{left:0;top:115px;width:1200px;height:63px;background:var(--quill-blue);display:flex;justify-content:center;align-items:center}
.mainnav a{color:#fff;font-size:12.5px;font-weight:500;text-decoration:none;padding:0 19px;height:63px;display:flex;align-items:center;border-right:1px solid rgba(255,255,255,.15)}
.mainnav a:last-child{border-right:none}

/* hero */
.hero-bg{left:0;top:178px;width:1200px;height:732px;background:linear-gradient(180deg,#1e3040 0%,#273c4c 45%,#141a26 100%)}
.hero-cut{position:absolute;left:0;top:178px;width:1200px;height:732px}
.hero-title{left:0;width:1200px;top:390px;text-align:center;color:#fff}
.hero-title .name{font-size:130px;font-weight:700;line-height:1;letter-spacing:-2px}
.hero-title .tag{font-size:58px;font-weight:400;line-height:1.1;margin-top:4px}
.btn-start{left:499px;top:608px;width:202px;height:60px;border-radius:30px;background:var(--quill-orange);color:#fff;font-size:22px;font-weight:500;display:flex;align-items:center;justify-content:center}
.dots{left:576px;top:822px;display:flex;gap:7px}
.dots i{width:11px;height:11px;border-radius:50%;background:#fff;display:block}
.dots i.on{background:var(--quill-orange)}

/* section titles */
.ghost{left:0;width:1200px;text-align:center;font-size:130px;font-weight:700;color:var(--faint);line-height:1;letter-spacing:2px}
.ghost.dark{color:rgba(255,255,255,.05)}
.stitle{left:0;width:1200px;text-align:center;font-size:46px;font-weight:600;color:var(--quill-blue);line-height:1}
.stitle.light{color:#fff}
.rule{left:576px;width:48px;height:3px;background:var(--quill-orange)}

/* about */
.about-lead{left:260px;width:680px;top:1060px;text-align:center;font-size:14.5px;line-height:31px;color:#333}
.portrait{left:122px;top:1180px;width:436px;height:436px;border-radius:50%;background:radial-gradient(circle at 40% 40%,#e6b9a0 0%,#b85a3c 45%,#3b2a3a 100%);border:5px solid var(--quill-orange)}
.about-body{left:610px;top:1204px;width:462px;font-size:13.5px;line-height:28px;color:#666;text-align:justify}
.about-body p+p{margin-top:26px}
.btn-learn{left:608px;top:1490px;width:196px;height:62px;border-radius:31px;background:var(--quill-blue);color:#fff;font-size:16px;display:flex;align-items:center;justify-content:center}

/* news */
.card{width:313px}
.card .photo{height:238px;background:linear-gradient(160deg,#6b5548,#2c2530 70%);position:relative}
.card .meta{position:absolute;left:12px;bottom:-4px;background:var(--quill-orange);color:#fff;font-size:13px;padding:6px 12px}
.card h3{color:#fff;font-size:21px;font-weight:500;margin-top:40px;line-height:26px}
.card p{color:#e3e3ee;font-size:12.5px;line-height:24px;margin-top:14px;text-align:justify}

/* events */
.event-photo{left:111px;top:2649px;width:515px;height:465px;background:linear-gradient(180deg,#9aa09a 0%,#6a4030 50%,#2b1a16 100%)}
.event-photo .cap{position:absolute;left:26px;bottom:30px;color:#fff}
.event-photo .date{color:var(--quill-orange);font-size:22px;font-weight:500}
.event-photo .ttl{font-size:26px;font-weight:500;line-height:32px}
.event-photo .desc{font-size:13px;margin-top:10px}
.event{left:652px;width:437px;height:132px;border:2px solid #e6e6ec;display:flex;align-items:center;padding:0 18px;gap:20px;background:#fff}
.event .badge{flex:none;width:92px;height:92px;border-radius:50%;color:#fff;text-align:center;display:flex;flex-direction:column;justify-content:center;line-height:1}
.event .badge b{font-size:40px;font-weight:500}
.event .badge span{font-size:24px;margin-top:2px}
.badge.orange{background:var(--quill-orange)}
.badge.blue{background:var(--quill-blue)}
.event h4{font-size:16px;font-weight:600;color:var(--quill-blue);line-height:24px}
.event p{font-size:12.5px;color:#777;line-height:20px;margin-top:6px}

/* testimonial */
.client-badge{left:242px;top:3296px;width:200px;height:200px;border-radius:50%;background:#fff;border:6px solid var(--quill-blue);display:flex;align-items:center;justify-content:center;color:var(--quill-blue);font-size:32px;font-weight:700}
.quote{left:517px;top:3300px;width:502px;color:#fff;font-size:14px;line-height:30px}
.quote .who{font-size:19px;font-weight:500;margin-top:12px;line-height:26px}
.quote .role{font-size:14px;color:#ffe0cc;line-height:20px}
.arrow{width:36px;height:36px;border-radius:50%;border:2px solid #fff;display:flex;align-items:center;justify-content:center}

/* organisations */
.org{width:156px;height:156px;border-radius:50%;background:#fff;box-shadow:0 0 18px rgba(244,116,36,.14);display:flex;align-items:center;justify-content:center;text-align:center;font-size:17px;font-weight:600;color:var(--quill-blue);line-height:1.1}

/* footer */
.foot-brand{left:0;width:1200px;top:4500px;text-align:center;color:#fff;font-size:90px;font-weight:700;line-height:1;letter-spacing:-2px}
.foot-contact{left:0;width:1200px;top:4614px;display:flex;justify-content:center;gap:30px;color:#fff;font-size:14.5px;align-items:center}
.foot-contact .ic{display:inline-flex;gap:8px;align-items:center}
.socials{left:472px;top:4670px;display:flex;gap:13px}
.socials i{width:40px;height:40px;border-radius:50%;border:2px solid #fff;display:block}
.copy{left:0;width:1200px;top:4746px;text-align:center;color:#fff;font-size:15px}
.copy span{color:var(--quill-orange)}
</style>
</head>
<body>
<div class="page">

  <!-- shaped bands -->
  <svg class="slants" viewBox="0 0 1200 4812" aria-hidden="true">
    <!-- news band -->
    <polygon points="0,1654 1200,1610 1200,2375 0,2440" fill="#f47424"/>
    <polygon points="0,1730 1200,1620 1200,2380 0,2440" fill="#231f5c"/>
    <polygon points="0,2440 1200,2375 1200,2440" fill="#ffffff"/>
    <polygon points="700,2410 1200,2372 1200,2400" fill="#f47424"/>
    <!-- testimonial -->
    <rect x="0" y="3205" width="1200" height="383" fill="#f47424"/>
    <polygon points="0,3205 285,3205 415,3588 0,3588" fill="#231f5c"/>
    <!-- footer -->
    <polygon points="0,4372 1200,4370 1200,4812 0,4812" fill="#f47424"/>
    <polygon points="0,4425 1200,4370 1200,4812 0,4812" fill="#231f5c"/>
  </svg>

  <!-- header -->
  <div class="abs brand">quill.</div>
  <div class="abs topbar">
    <span class="ic"><svg width="13" height="13" viewBox="0 0 24 24"><path d="M6.6 10.8a15 15 0 006.6 6.6l2.2-2.2c.3-.3.7-.4 1-.2 1.1.4 2.3.6 3.6.6.6 0 1 .4 1 1V20c0 .6-.4 1-1 1A17 17 0 013 4c0-.6.4-1 1-1h3.5c.6 0 1 .4 1 1 0 1.3.2 2.5.6 3.6.1.3 0 .7-.2 1z" fill="#f47424"/></svg>Call Us : 022 555 0147</span>
    <span class="ic"><svg width="14" height="12" viewBox="0 0 24 20"><rect x="1" y="1" width="22" height="18" rx="2" fill="none" stroke="#f47424" stroke-width="2"/><path d="M1 2l11 9 11-9" fill="none" stroke="#f47424" stroke-width="2"/></svg>hello@quill-example.co.nz</span>
    <span class="home">HOME</span>
    <span class="about">ABOUT US</span>
    <span class="btn-contact">CONTACT US</span>
  </div>
  <nav class="abs mainnav">
    <a>WHO WE ARE</a><a>HOW WE CAN HELP</a><a>WHERE WE COME FROM</a><a>WORKING WITH QUILL</a><a>QUILL COMMUNITY</a><a>NEWS</a><a>EVENTS</a>
  </nav>

  <!-- hero -->
  <div class="abs hero-bg" role="img" aria-label="Night city street with glowing shop signs"></div>
  <svg class="hero-cut" viewBox="0 0 1200 732" aria-hidden="true">
    <polygon points="0,732 1200,612 1200,732" fill="#ffffff"/>
    <polygon points="780,682 1200,612 1200,672" fill="#f47424"/>
  </svg>
  <div class="abs hero-title"><div class="name">quill</div><div class="tag">People with expertise</div></div>
  <div class="abs btn-start">Get Started</div>
  <div class="abs dots"><i></i><i class="on"></i><i></i></div>

  <!-- about -->
  <div class="abs ghost" style="top:930px">ABOUT US</div>
  <div class="abs stitle" style="top:988px">ABOUT US</div>
  <div class="abs rule" style="top:1046px"></div>
  <p class="abs about-lead">Great PR is built on excellent communication and strong relationships. That's what we do. We offer strategic advice and hands-on advocacy support to ensure you are heard and understood by the public, media and stakeholders.</p>
  <div class="abs portrait" role="img" aria-label="Profile photo of the two founders"></div>
  <div class="abs about-body">
    <p>Clara Whitford and Jane Morrow more have worked in and around communications and politics for over a decade. They will ensure your voice and story is heard by the right people to have maximum impact.</p>
    <p>Clara's experience spans the public, private and non-government sectors in both New Zealand and Australia. Her expertise is in domestic and international media management, campaigns, change strategic communications and government relations.</p>
  </div>
  <div class="abs btn-learn">LEARN MORE</div>

  <!-- news -->
  <div class="abs ghost dark" style="top:1720px">NEWS</div>
  <div class="abs stitle light" style="top:1786px">LATEST NEWS</div>
  <div class="abs rule" style="top:1842px"></div>
  <article class="abs card" style="left:111px;top:1878px">
    <div class="photo" role="img" aria-label="Guests talking at a media event"><span class="meta">May 27, 2022 Clara Whitford</span></div>
    <h3>Tips from the Newsroom</h3>
    <p>Tips from the newsroom - our June media work shop will be hosted by former Brightwater Gazette and Kestrel Daily reporter Tess Carver and will focus on how to get in today's media environment.</p>
  </article>
  <article class="abs card" style="left:445px;top:1878px">
    <div class="photo" role="img" aria-label="People mingling at an evening function"><span class="meta">May 2, 2022 Jane Morrow</span></div>
    <h3>Have you heard the news?</h3>
    <p>Tips from the newsroom - our June media work shop will be hosted by former Brightwater Gazette and Kestrel Daily reporter Tess Carver and will focus on how to get in today's media environment.</p>
  </article>
  <article class="abs card" style="left:778px;top:1878px">
    <div class="photo" role="img" aria-label="Seated audience in a panelled room"><span class="meta">Mar 3, 2022 Owen Hale</span></div>
    <h3>Get the most out of your comms in 2022</h3>
    <p style="margin-top:8px">In 2022, the impact of the pandemic continues to touch every aspect of life and business in Aotearoa. With the right angle directed..</p>
  </article>

  <!-- events -->
  <div class="abs ghost" style="top:2478px">EVENTS</div>
  <div class="abs stitle" style="top:2530px">UPCOMING EVENTS</div>
  <div class="abs event-photo" role="img" aria-label="Meeting room with armchairs and a flower arrangement">
    <div class="cap"><div class="date">MAY 12, 2022</div><div class="ttl">BIM WRITING 101</div><div class="desc">Election season starts early in politics, and before you know it..</div></div>
  </div>
  <div class="abs event" style="top:2655px"><div class="badge orange"><b>12</b><span>MAY</span></div><div><h4>TIPS FROM THE NEWSROOM MEDIA WORKSHOP</h4><p>Join former senior editor and journalist Tess Carver this interactive Media 101 workshop.</p></div></div>
  <div class="abs event" style="top:2812px"><div class="badge blue"><b>15</b><span>MAY</span></div><div><h4>BIM WRITING 101</h4><p>Election season starts early in politics, and before you know it, it's BIM time again.</p></div></div>
  <div class="abs event" style="top:2968px"><div class="badge orange"><b>18</b><span>MAY</span></div><div><h4>TIPS FROM THE NEWSROOM MEDIA WORKSHOP</h4><p>Join former senior editor and journalist Tess Carver this interactive Media 101 workshop.</p></div></div>

  <!-- testimonial -->
  <div class="abs arrow" style="left:66px;top:3377px"><svg width="12" height="12" viewBox="0 0 12 12"><path d="M8 1L3 6l5 5" fill="none" stroke="#fff" stroke-width="2"/></svg></div>
  <div class="abs client-badge">mendwell</div>
  <div class="abs quote">
    <p>With their depth of knowledge and experience Jane and the Quill team have provided Mendwell with invaluable guidance as we represent our community. We are so grateful for their professionalism and expertise, enabling us to advocate for those suffering while we carry out our vital work of supporting families.</p>
    <div class="who">Ruth Palmer</div>
    <div class="role">Chair,Mendwell</div>
  </div>
  <div class="abs arrow" style="left:1096px;top:3377px"><svg width="12" height="12" viewBox="0 0 12 12"><path d="M4 1l5 5-5 5" fill="none" stroke="#fff" stroke-width="2"/></svg></div>

  <!-- organisations -->
  <div class="abs ghost" style="top:3632px">ORGANISATION</div>
  <div class="abs stitle" style="top:3680px">ORGANISATIONS WITH QUILL</div>
  <div class="abs org" style="left:127px;top:3792px">Kindred Crew</div>
  <div class="abs org" style="left:327px;top:3792px">Case Review Office</div>
  <div class="abs org" style="left:522px;top:3792px">Tui Hub</div>
  <div class="abs org" style="left:727px;top:3792px">Transit Office</div>
  <div class="abs org" style="left:927px;top:3792px">Fairness Office</div>
  <div class="abs org" style="left:222px;top:3962px">RoadWise</div>
  <div class="abs org" style="left:422px;top:3962px">mendwell</div>
  <div class="abs org" style="left:622px;top:3962px">Lakeside</div>
  <div class="abs org" style="left:822px;top:3962px">Studio Nine</div>
  <div class="abs org" style="left:127px;top:4137px">Skylark Air</div>
  <div class="abs org" style="left:327px;top:4137px">Coastline Minerals</div>
  <div class="abs org" style="left:522px;top:4137px">Harrow Trust</div>
  <div class="abs org" style="left:727px;top:4137px">Truepath</div>
  <div class="abs org" style="left:927px;top:4137px">Forest Fund</div>

  <!-- footer -->
  <div class="abs foot-brand">quill.</div>
  <div class="abs foot-contact">
    <span class="ic"><svg width="11" height="14" viewBox="0 0 12 16"><path d="M6 0a6 6 0 016 6c0 4.5-6 10-6 10S0 10.5 0 6a6 6 0 016-6z" fill="#f47424"/><circle cx="6" cy="6" r="2.2" fill="#231f5c"/></svg>Harbour House &nbsp;Suite 9, 40 Sample Road Harbourton 9999</span>
    <span>/</span>
    <span class="ic"><svg width="14" height="12" viewBox="0 0 24 20"><rect x="1" y="1" width="22" height="18" rx="2" fill="none" stroke="#f47424" stroke-width="2"/><path d="M1 2l11 9 11-9" fill="none" stroke="#f47424" stroke-width="2"/></svg>hello@quill-example.co.nz</span>
    <span>/</span>
    <span class="ic"><svg width="13" height="13" viewBox="0 0 24 24"><path d="M6.6 10.8a15 15 0 006.6 6.6l2.2-2.2c.3-.3.7-.4 1-.2 1.1.4 2.3.6 3.6.6.6 0 1 .4 1 1V20c0 .6-.4 1-1 1A17 17 0 013 4c0-.6.4-1 1-1h3.5c.6 0 1 .4 1 1 0 1.3.2 2.5.6 3.6.1.3 0 .7-.2 1z" fill="#f47424"/></svg>022 555 0147</span>
  </div>
  <div class="abs socials" aria-label="Social links"><i></i><i></i><i></i><i></i><i></i></div>
  <div class="abs copy">© Copyright 2022 <span>Quill Communications</span>.All Rights Reserved</div>

</div>
</body>
</html>
```